International Flower distributer needs a landing page

We are looking to have a landing page made that will be easy to maintain and upload more content as our business grows.

We like the template designs and ease of use of Pagewright. We'd explore other host sites.

Hello,

To start we would like something that can be managed and updated on a platform like pagewright. We like page wright because of the premade designs and flexibility.

Website requirements:

- About us:

- Marlowe Vantage Corp - Established 1999

- Verna Holt - Founder

- Danielle Holt - Account Executive

- Gregory Holt - Director of Operations

- Pilar Wendham - (Jo's Job Description?)

- Renata Valcourt (Make us look like a bigger company with more staff)

What we do:

- Personalized Customer service

- Exclusively Mass market experience to meet high demands

- Dedicated team assigned to your account

How we do it:

- Partnerships with farms in COlombia, ecuador and costa rica

- Farm fresh delivered directly from cargo planes to state of the art cooler facility at Delmont Airport

- Verity Trust?

Products we Sell:

- Farm made bouquets

- Consumer Bunches

- Programs Tailored to fit customer's retail program

For more Information:

- Gregory and Danielle phone and email

- Submit email inquiry

Gathering more feedback

Corporate buyers that want to verify who we are and get our contact information

Floral, but not a flower shop. We import farm fresh cut flowers from south america and send them directly to supermarkets around the country.

• We are not selling anything on the website. We sell business to business.

```html
<!DOCTYPE html>
<html lang="en">
<head>
<meta charset="utf-8">
<title>Marlowe Vantage — Flower Distribution</title>
<link rel="stylesheet" href="https://fonts.googleapis.com/css2?family=Arimo:wght@400;700&family=Lato:wght@400;700&display=swap">
<style>
:root{
  --green:#7dc13a;
  --green-dark:#5e9b2a;
  --navy:#232493;
  --navy-deep:#1a1b7d;
  --band:#26289a;
  --ink:#1b1b1b;
  --text:#3b3b3b;
  --grey-track:#c3cad8;
  --black:#000;
  --white:#fff;
}
*{box-sizing:border-box;margin:0;padding:0}
html,body{width:1200px;height:4270px;overflow:hidden}
body{position:relative;background:var(--white);font-family:"Lato",sans-serif;color:var(--text)}
.abs{position:absolute}
h2.section-title{position:absolute;left:0;width:1200px;text-align:center;font-family:"Arimo",sans-serif;font-weight:700;font-size:34px;color:var(--ink);letter-spacing:.5px}
.btn{position:absolute;display:flex;align-items:center;justify-content:center;gap:9px;background:var(--green);color:var(--white);font-family:"Arimo",sans-serif;font-weight:700;font-size:15px;border-radius:20px}
.btn i{width:13px;height:13px;border-radius:50%;background:var(--white);position:relative}
.btn i::after{content:"";position:absolute;left:3px;top:4px;border-left:5px solid var(--green);border-top:3px solid transparent;border-bottom:3px solid transparent;margin-left:1px}

/* nav */
.topline{left:0;top:0;width:1200px;height:4px;background:var(--green)}
.navbar{left:0;top:4px;width:1200px;height:71px;background:var(--white);z-index:3}
.nav-links{position:absolute;left:271px;top:28px;display:flex;gap:24px;font-family:"Arimo",sans-serif;font-weight:700;font-size:14px;color:var(--ink)}
.nav-links .active{color:var(--green);border-bottom:2px solid var(--green);padding-bottom:4px}
.login{left:996px;top:22px;width:102px;height:34px;font-size:14px}
.brand-badge{left:102px;top:0;width:140px;height:140px;border-radius:50%;background:var(--white);z-index:4;display:flex;align-items:center;justify-content:center;flex-direction:column;gap:6px}
.brand-badge span{font-family:"Arimo",sans-serif;font-weight:700;font-size:14px;color:var(--navy);letter-spacing:1px;text-align:center;line-height:1.2;margin-top:20px}
.brand-badge b{width:22px;height:22px;border-radius:50%;background:var(--green)}

/* hero */
.hero{left:0;top:75px;width:1200px;height:720px;overflow:hidden}
.hero-photo{position:absolute;inset:0;background:linear-gradient(120deg,#8f8a6f 0%,#6d7a5a 30%,#a79d8f 55%,#5d6d48 80%,#8a9466 100%)}
.hero-shade{position:absolute;inset:0;background:rgba(20,20,20,.25)}
.hero h1{position:absolute;left:0;top:295px;width:1200px;text-align:center;font-family:"Arimo",sans-serif;font-weight:700;font-size:54px;color:var(--white);letter-spacing:1px}
.hero p{position:absolute;left:300px;top:370px;width:600px;text-align:center;font-size:15px;line-height:27px;color:var(--white)}
.hero .btn{left:517px;top:447px;width:166px;height:40px}
.hero-wave{position:absolute;left:0;top:0}
.dots{position:absolute;left:566px;top:627px;display:flex;gap:14px;align-items:center}
.dots i{width:10px;height:10px;background:var(--white);transform:rotate(45deg)}
.dots i.on{width:16px;height:16px;background:var(--green)}

/* what we do */
.wwd-bg{left:0;top:1300px;width:1200px;height:274px;background:linear-gradient(#fff,#f3f4f6)}
.wwd-art{left:0;top:940px}
.step-caption{position:absolute;top:1446px;width:240px;text-align:center;font-size:15px;line-height:26px;color:var(--text)}

/* about */
.about{left:0;top:1574px;width:1200px;height:472px;background:linear-gradient(90deg,#e6e7ea,#d9dbdf)}
.about-photo{position:absolute;left:0;top:0;width:530px;height:472px;background:radial-gradient(circle at 45% 45%,#f08a3c 0%,#ef6f8f 30%,#f5b84a 50%,#dfe0e3 75%)}
.about h3{position:absolute;left:633px;top:50px;font-family:"Arimo",sans-serif;font-weight:700;font-size:34px;color:var(--ink)}
.about p{position:absolute;left:633px;top:110px;width:460px;font-size:15px;line-height:25.8px;color:var(--text)}
.about .btn{left:633px;top:374px;width:166px;height:40px}

/* products */
.product{position:absolute;top:2197px;width:282px;height:308px;color:var(--white);text-align:center}
.product.navy{background:var(--navy)}
.product.green{background:var(--green)}
.product svg.icon{position:absolute;left:106px;top:30px}
.product h4{position:absolute;left:0;top:128px;width:100%;font-family:"Arimo",sans-serif;font-weight:700;font-size:15px}
.product p{position:absolute;left:14px;top:158px;width:254px;font-size:14.5px;line-height:26px}
.product .go{position:absolute;left:128px;top:249px;width:26px;height:26px;border-radius:50%;background:var(--white)}
.product .go::after{content:"";position:absolute;left:7px;top:9px;width:6px;height:6px;border-top:2px solid var(--ink);border-right:2px solid var(--ink);transform:rotate(45deg)}

/* how */
.how{left:0;top:2588px;width:1200px;height:514px;background:var(--band)}
.how h2.section-title{top:60px;color:var(--white)}
.how-item{position:absolute;top:152px;width:300px;height:300px}
.how-photo{position:absolute;left:22px;top:22px;width:256px;height:256px;border-radius:50%;border:6px solid var(--white)}
.how-text{position:absolute;left:40px;top:0;width:220px;height:300px;display:flex;flex-direction:column;align-items:center;justify-content:center;text-align:center;color:var(--white);font-family:"Arimo",sans-serif;font-size:15px;line-height:26px}
.how-text em{font-style:normal;color:var(--green);font-size:14px;display:flex;align-items:center;gap:6px}
.how-text em i{width:12px;height:12px;border-radius:50%;background:var(--green)}

/* news */
.news{position:absolute;top:3248px;width:438px}
.news-photo{width:438px;height:255px}
.news-date{position:absolute;left:-6px;top:264px;width:20px;height:90px;writing-mode:vertical-rl;transform:rotate(180deg);font-size:11px;color:var(--green);font-family:"Arimo",sans-serif;font-weight:700;border-left:2px solid var(--green);text-align:center}
.news h5{position:absolute;left:25px;top:274px;width:410px;font-family:"Arimo",sans-serif;font-weight:700;font-size:13.5px;line-height:24px;color:var(--ink)}
.news p{position:absolute;left:25px;top:323px;width:410px;font-size:14.5px;line-height:26px;color:var(--text)}
.news-meta{position:absolute;left:0;top:407px;width:430px;display:flex;justify-content:space-between;font-family:"Arimo",sans-serif;font-weight:700;font-size:12.5px;color:var(--green)}
.news-meta span{display:flex;align-items:center;gap:6px}
.news-meta i{width:9px;height:9px;border-radius:50%;background:var(--green)}

/* footer */
.footer-wave{left:0;top:3731px}
.footer{left:0;top:3930px;width:1200px;height:340px;background:var(--black);color:var(--white)}
.footer h6{position:absolute;font-family:"Arimo",sans-serif;font-weight:700;font-size:15px;text-decoration:underline;text-underline-offset:4px}
.footer ul{position:absolute;list-style:none;font-size:15px}
.footer li{display:flex;gap:14px;align-items:center}
.footer li::before{content:"»";font-size:15px}
.foot-brand{position:absolute;left:111px;top:22px;width:90px;text-align:center;font-family:"Arimo",sans-serif;font-weight:700;font-size:13px;letter-spacing:1px;line-height:1.3}
.foot-brand b{display:block;width:14px;height:14px;border-radius:50%;background:var(--white);margin:0 auto 6px}
.foot-about{position:absolute;left:111px;top:130px;width:260px;font-size:14.5px;line-height:28px}
.socials{position:absolute;left:111px;top:227px;display:flex;gap:8px}
.socials i{width:32px;height:32px;border-radius:50%}
.contact-row{position:absolute;left:878px;display:flex;align-items:center;gap:18px;font-size:14.5px;line-height:22px}
.contact-row .ring{width:32px;height:32px;border-radius:50%;border:2px solid var(--white);display:flex;align-items:center;justify-content:center;flex:none}
.foot-rule{position:absolute;left:111px;top:288px;width:1045px;height:1px;background:#444}
.copyright{position:absolute;left:0;top:308px;width:1200px;text-align:center;font-size:13px}
</style>
</head>
<body>

<div class="abs topline"></div>
<header class="abs navbar">
  <nav class="nav-links">
    <span class="active">HOME</span><span>ABOUT US</span><span>WHAT WE DO</span><span>HOW WE DO IT</span><span>PRODUCTS WE SELL</span><span>CONTACT US</span>
  </nav>
  <div class="btn login">LOGIN <i></i></div>
</header>
<div class="abs brand-badge"><span>MARLOWE<br>VANTAGE</span><b></b></div>

<section class="abs hero">
  <div class="hero-photo" role="img" aria-label="Florist carrying bouquets on a tree-lined street"></div>
  <div class="hero-shade"></div>
  <h1>MARLOWE VANTAGE</h1>
  <p>Lorem ipsum dolor sit amet, consectetur adipiscing elit, sed eiusmod tempor labore et dolore magna aliqua. Ut enim ad minim veniam, quis nostrud exercitation</p>
  <div class="btn">GET STARTED <i></i></div>
  <svg class="hero-wave" width="1200" height="720" viewBox="0 0 1200 720">
    <path d="M0 538 Q600 900 1200 530 L1200 720 L0 720Z" fill="var(--green)"/>
    <path d="M0 570 Q600 885 1200 562 L1200 720 L0 720Z" fill="var(--white)"/>
  </svg>
  <div class="dots"><i></i><i class="on"></i><i></i></div>
</section>

<h2 class="section-title" style="top:878px">WHAT WE DO</h2>
<div class="abs wwd-bg"></div>
<svg class="abs wwd-art" width="1200" height="560" viewBox="0 940 1200 560">
  <defs>
    <linearGradient id="waveGrad" x1="140" y1="0" x2="1060" y2="0" gradientUnits="userSpaceOnUse">
      <stop offset="0" stop-color="#1d2a8a"/><stop offset=".3" stop-color="#273f78"/><stop offset=".55" stop-color="#3f7a52"/><stop offset="1" stop-color="#7dc13a"/>
    </linearGradient>
    <radialGradient id="p1"><stop offset="0" stop-color="#e63a4a"/><stop offset="1" stop-color="#9c1d2d"/></radialGradient>
    <radialGradient id="p2"><stop offset="0" stop-color="#e7d9c8"/><stop offset=".6" stop-color="#7cb342"/><stop offset="1" stop-color="#2f4a2a"/></radialGradient>
    <radialGradient id="p3"><stop offset="0" stop-color="#f1a48f"/><stop offset=".6" stop-color="#eeeeee"/><stop offset="1" stop-color="#8a9a8c"/></radialGradient>
  </defs>
  <path d="M311 988 A155 155 0 1 0 466 1143 A139 139 0 0 1 744 1143 A153 153 0 0 0 1050 1143" fill="none" stroke="url(#waveGrad)" stroke-width="34"/>
  <line x1="182" y1="1400" x2="1039" y2="1400" stroke="var(--grey-track)" stroke-width="18" stroke-linecap="round"/>
  <line x1="311" y1="1260" x2="311" y2="1400" stroke="var(--navy-deep)" stroke-width="6"/>
  <line x1="605" y1="1275" x2="605" y2="1400" stroke="var(--green)" stroke-width="6"/>
  <line x1="895" y1="1275" x2="895" y2="1400" stroke="var(--navy-deep)" stroke-width="6"/>
  <g stroke="#fff" stroke-width="8">
    <circle cx="311" cy="1143" r="112" fill="url(#p1)" role="img" aria-label="Red peony bouquet"/>
    <circle cx="605" cy="1143" r="112" fill="url(#p2)" role="img" aria-label="Mixed green and white flower arrangement"/>
    <circle cx="895" cy="1143" r="112" fill="url(#p3)" role="img" aria-label="Wrapped bouquet of carnations and roses"/>
  </g>
  <g font-family="Arimo, sans-serif" font-weight="700" font-size="14" fill="#fff" text-anchor="middle">
    <circle cx="311" cy="1401" r="26" fill="#dfe3ea"/><circle cx="311" cy="1401" r="18" fill="var(--navy-deep)"/><text x="311" y="1406">1</text>
    <circle cx="605" cy="1401" r="26" fill="#dfe3ea"/><circle cx="605" cy="1401" r="18" fill="var(--green)"/><text x="605" y="1406">2</text>
    <circle cx="895" cy="1401" r="26" fill="#dfe3ea"/><circle cx="895" cy="1401" r="18" fill="var(--navy-deep)"/><text x="895" y="1406">3</text>
  </g>
</svg>
<div class="step-caption" style="left:191px">Personalized Customer<br>service</div>
<div class="step-caption" style="left:465px;width:280px">Exclusively Mass market<br>experience to meet high demands</div>
<div class="step-caption" style="left:775px">Dedicated team assigned<br>to your account</div>

<section class="abs about">
  <div class="about-photo" role="img" aria-label="Colourful ranunculus, tulip and poppy bouquet with pink ribbon"></div>
  <h3>ABOUT US</h3>
  <p>Lorem ipsum dolor sit amet, consectetur adipiscing elit, &nbsp;eiusmod tempor incididunt ut labore et dolore magna aliqua.enim ad minim veniam, quis nostrud exercitation ullamco laboris nisi ut aliquip ex commodo consequat.Duis aute irure dolor reprehenderit voluptate velit esse cillum dolore fugiat nulla pariatur Excepteur sint occacat cupidatat non proident sunt in culpa qui officia deserunt architecto beatae vitae dicta sunt explicabemo enim ipsam voluptatem queia voluptas sit aspernatur aut odit aut fugit, sed quia ut consequuntur magni dolores eos qumollit anim id estdolor sunt ut &nbsp;laborum.</p>
  <div class="btn">LEARN MORE <i></i></div>
</section>

<h2 class="section-title" style="top:2124px">PRODUCTS WE SELL</h2>
<svg width="0" height="0" style="position:absolute">
  <defs>
    <symbol id="bouquet" viewBox="0 0 70 80">
      <circle cx="22" cy="20" r="11" fill="currentColor"/>
      <circle cx="48" cy="20" r="11" fill="currentColor"/>
      <circle cx="35" cy="12" r="11" fill="currentColor"/>
      <circle cx="35" cy="32" r="10" fill="currentColor"/>
      <path d="M22 42 L48 42 L38 78 L32 78Z" fill="currentColor"/>
    </symbol>
  </defs>
</svg>
<div class="product navy" style="left:161px">
  <svg class="icon" width="70" height="80" style="color:#fff"><use href="#bouquet"/></svg>
  <h4>FARM MADE BOUQUETS</h4>
  <p>Lorem ipsum dolor &nbsp;amet consectetur adipiscing elitsed &nbsp;eiusmod tempor sed do eiusmod tincididunt</p>
  <span class="go"></span>
</div>
<div class="product green" style="left:459px">
  <svg class="icon" width="70" height="80" style="color:#fff"><use href="#bouquet"/></svg>
  <h4>CONSUMER BUNCHES</h4>
  <p>Lorem ipsum dolor &nbsp;amet consectetur adipiscing elitsed &nbsp;eiusmod tempor sed do eiusmod tincididunt</p>
  <span class="go"></span>
</div>
<div class="product navy" style="left:757px">
  <svg class="icon" width="70" height="80" style="color:#fff"><use href="#bouquet"/></svg>
  <h4>TAILORED RETAIL PROGRAMS</h4>
  <p>Lorem ipsum dolor &nbsp;amet consectetur adipiscing elitsed &nbsp;eiusmod tempor sed do eiusmod tincididunt</p>
  <span class="go"></span>
</div>

<section class="abs how">
  <h2 class="section-title">HOW WE DO IT</h2>
  <div class="how-item" style="left:127px">
    <svg class="abs" width="300" height="300" viewBox="0 0 300 300"><circle cx="150" cy="150" r="142" fill="none" stroke="var(--green)" stroke-width="9" stroke-dasharray="660 232" transform="rotate(-110 150 150)"/></svg>
    <div class="how-photo" role="img" aria-label="Farm arrangement of green and white blooms" style="background:radial-gradient(circle,#6f7e6a,#3f5a3a)"></div>
    <div class="how-text"><b style="font-weight:400">PARTNERSHIPS WITH<br>FARMS IN COLOMBIA,<br>ECUADOR</b></div>
  </div>
  <div class="how-item" style="left:450px">
    <svg class="abs" width="300" height="300" viewBox="0 0 300 300"><circle cx="150" cy="150" r="142" fill="none" stroke="var(--green)" stroke-width="9" stroke-dasharray="660 232" transform="rotate(-110 150 150)"/></svg>
    <div class="how-photo" role="img" aria-label="Fresh cut flowers in a cooler facility" style="background:radial-gradient(circle,#3d2a6a,#1e1f6f)"></div>
    <div class="how-text" style="font-size:14px">Farm fresh delivered directly from cargo planes to state of the art cooler facility at Delmont Airport<em>Read More <i></i></em></div>
  </div>
  <div class="how-item" style="left:775px">
    <svg class="abs" width="300" height="300" viewBox="0 0 300 300"><circle cx="150" cy="150" r="142" fill="none" stroke="var(--green)" stroke-width="9" stroke-dasharray="660 232" transform="rotate(-110 150 150)"/></svg>
    <div class="how-photo" role="img" aria-label="Yellow sunflowers and cream roses" style="background:radial-gradient(circle,#b59a4a,#6e6a3c)"></div>
    <div class="how-text">VERITY TRUST</div>
  </div>
</section>

<h2 class="section-title" style="top:3181px">LATEST NEWS</h2>
<article class="news" style="left:144px">
  <div class="news-photo" role="img" aria-label="Pink lily bouquet wrapped in paper" style="background:linear-gradient(135deg,#7c7565,#c98fa8 45%,#5f6e52)"></div>
  <div class="news-date">JUN,17,2022</div>
  <h5>LOREM IPSUM DOLOR CONSECTETUR ADIPISCING ELIT, SED DO EIUSMOD TEMPOR INCIDIDUNT UT</h5>
  <p>Lorem ipsum dolor sit amet, consectetur adipiscing elit, sed do eiusmod tempor incididunt ut labore et dolore</p>
  <div class="news-meta"><span><i></i>By Admin</span><span><i></i>Comments</span></div>
</article>
<article class="news" style="left:618px">
  <div class="news-photo" role="img" aria-label="White and red rose bridal bouquets" style="background:linear-gradient(135deg,#3a3a3c,#d9d6d2 45%,#6d2430 70%,#2f3a2f)"></div>
  <div class="news-date">JUN,17,2022</div>
  <h5>LOREM IPSUM DOLOR CONSECTETUR ADIPISCING ELIT, SED DO EIUSMOD TEMPOR INCIDIDUNT UT</h5>
  <p>Lorem ipsum dolor sit amet, consectetur adipiscing elit, sed do eiusmod tempor incididunt ut labore et dolore</p>
  <div class="news-meta"><span><i></i>By Admin</span><span><i></i>Comments</span></div>
</article>

<svg class="abs footer-wave" width="1200" height="200" viewBox="0 0 1200 200">
  <path d="M0 170 Q600 -130 1200 170 L1200 200 L0 200Z" fill="var(--green)"/>
  <path d="M0 200 Q600 -80 1200 200 Z" fill="var(--black)"/>
</svg>
<footer class="abs footer">
  <div class="foot-brand"><b></b>MARLOWE<br>VANTAGE</div>
  <p class="foot-about">Lorem ipsum dolor utconsectetur adipiscing elit ut &nbsp;sed do eiusmod</p>
  <h6 style="left:111px;top:196px">FOLLOW ON</h6>
  <div class="socials"><i style="background:#1f2a8c"></i><i style="background:#2a9ee0"></i><i style="background:#e02424"></i><i style="background:#9c7b45"></i></div>

  <h6 style="left:437px;top:26px">OTHER LINKS</h6>
  <ul style="left:437px;top:62px"><li style="height:30px">Team</li><li style="height:30px">FAQ</li><li style="height:30px">Services</li><li style="height:30px">Privacy</li><li style="height:30px">Policy</li></ul>

  <h6 style="left:645px;top:26px">QUICK LINKS</h6>
  <ul style="left:645px;top:62px"><li style="height:37px">Home</li><li style="height:37px">About Us</li><li style="height:37px">What we do</li><li style="height:37px">How we do it</li><li style="height:37px">Products we Sell</li><li style="height:37px">Contact Us</li></ul>

  <h6 style="left:878px;top:26px">CONTACT US</h6>
  <div class="contact-row" style="top:60px"><span class="ring"><svg width="14" height="14" viewBox="0 0 24 24"><path d="M6.6 10.8a15 15 0 0 0 6.6 6.6l2.2-2.2a1 1 0 0 1 1-.25 11 11 0 0 0 3.6.6 1 1 0 0 1 1 1V20a1 1 0 0 1-1 1A17 17 0 0 1 3 4a1 1 0 0 1 1-1h3.5a1 1 0 0 1 1 1 11 11 0 0 0 .6 3.6 1 1 0 0 1-.25 1z" fill="#fff"/></svg></span>+ 555-0142-377</div>
  <div class="contact-row" style="top:120px"><span class="ring"><svg width="14" height="12" viewBox="0 0 24 18"><rect x="1" y="1" width="22" height="16" fill="none" stroke="#fff" stroke-width="2"/><path d="M1 1l11 9 11-9" fill="none" stroke="#fff" stroke-width="2"/></svg></span>info@marlowevantage.com</div>
  <div class="contact-row" style="top:180px"><span class="ring"><svg width="12" height="16" viewBox="0 0 24 32"><path d="M12 1a11 11 0 0 0-11 11c0 8 11 19 11 19s11-11 11-19A11 11 0 0 0 12 1z" fill="none" stroke="#fff" stroke-width="2.5"/><circle cx="12" cy="12" r="4" fill="#fff"/></svg></span>31,perspiciatis &nbsp;steunde<br>natus error sit voluptem</div>

  <div class="foot-rule"></div>
  <div class="copyright">© 2022 Copyrights &nbsp;Marlowe Vantage &nbsp;| &nbsp;All Rights Reserved.</div>
</footer>

</body>
</html>
```